Home Inspector

i do home inspections in Houston Texas. Would like a nice logo(maybe forest green and black). I inspect:foundations,structural,electric,plumbing,appliances,pools/spas and other optional systems.Hours mon-sat.

Industry/Entity Type

Plumbing

Contact Information for Business Card

BRIGHTWELL PROPERTY INSPECTIONS,5831 Tamsel Ridge,Houston,Texas,62958,Daniel Okafor,Professional Inspector,License#48276,Serving the Greater Houston Area

```html
<!DOCTYPE html>
<html lang="en">
<head>
<meta charset="utf-8">
<title>Brightwell Property Inspections – Business Card</title>
<link rel="stylesheet" href="https://fonts.googleapis.com/css2?family=Lato:wght@400;700;900&display=swap">
<style>
  :root {
    --forest: #1f4a2c;
    --forest-deep: #163a21;
    --ink: #1c1c1c;
    --paper: #ffffff;
    --divider: #d9d9d9;
    --backdrop: #e4e4e4;
  }
  * { box-sizing: border-box; margin: 0; padding: 0; }
  html, body {
    width: 1200px;
    height: 900px;
    overflow: hidden;
    background: var(--backdrop);
    font-family: "Lato", sans-serif;
  }
  .business-card {
    position: absolute;
    left: 100px;
    top: 164px;
    width: 1000px;
    height: 572px;
    background: var(--paper);
    overflow: hidden;
    box-shadow: 0 6px 24px rgba(0,0,0,0.12);
  }
  .brand {
    position: absolute;
    left: 110px;
    top: 175px;
    display: flex;
    align-items: center;
    gap: 22px;
  }
  .brand-dot {
    width: 78px;
    height: 78px;
    border-radius: 50%;
    background: var(--forest);
    flex: none;
  }
  .brand-name {
    font-weight: 700;
    color: var(--ink);
    font-size: 34px;
    line-height: 1.05;
    letter-spacing: 0.2px;
  }
  .divider {
    position: absolute;
    left: 530px;
    top: 95px;
    width: 2px;
    height: 300px;
    background: var(--divider);
  }
  .contact {
    position: absolute;
    left: 575px;
    top: 110px;
    color: var(--ink);
  }
  .person-name {
    font-size: 46px;
    font-weight: 400;
    letter-spacing: -0.5px;
    line-height: 1;
  }
  .person-name .surname { font-weight: 700; }
  .person-title {
    margin-top: 14px;
    font-size: 17px;
    font-weight: 900;
    letter-spacing: 2.4px;
    color: var(--forest);
  }
  .license {
    margin-top: 58px;
    font-size: 23px;
    font-weight: 700;
    letter-spacing: 2px;
  }
  .address {
    margin-top: 16px;
    font-size: 19px;
    line-height: 1.35;
    text-transform: uppercase;
  }
  .service-band {
    position: absolute;
    left: 0;
    bottom: 0;
    width: 1000px;
    height: 190px;
  }
  .service-tagline {
    position: absolute;
    left: 0;
    width: 860px;
    bottom: 42px;
    text-align: center;
    color: var(--paper);
    font-size: 24px;
    font-weight: 700;
    letter-spacing: 3.5px;
  }
</style>
</head>
<body>
  <div class="business-card">
    <div class="brand">
      <div class="brand-dot"></div>
      <div class="brand-name">Brightwell<br>Property<br>INSPECTIONS</div>
    </div>

    <div class="divider"></div>

    <div class="contact">
      <h1 class="person-name">Daniel <span class="surname">Okafor</span></h1>
      <p class="person-title">PROFESSIONAL INSPECTOR</p>
      <p class="license">LICENSE#48276</p>
      <p class="address">5831 Tamsel Ridge,<br>Houston, Texas, 62958</p>
    </div>

    <svg class="service-band" viewBox="0 0 1000 190" aria-hidden="true">
      <path d="M0,110 Q520,10 1000,70 L1000,190 L0,190 Z" fill="var(--forest-deep)"/>
    </svg>
    <p class="service-tagline">SERVING THE GREATER HOUSTON AREA</p>
  </div>
</body>
</html>
```